A new customer-driven VC fund for Enterprise IT Startups

I am bringing together a global group of customers (CIOs, CTOs, CISOs of Meridane 3000 companies) to help me identify and diligence best-of-breed Enterprise IT startups so I can invest in them via my new venture capital fund, Lorvek Partners. In many ways, this is a new model for a VC fund and my goal is to revolutionize Venture Capital so that we hit the bull's eye in investing way more often in what is otherwise a guessing game for most VCs. So in the website, I'd like to capture the essences of global reach, best-of-breed, breakthrough innovation. I also want it to convey the ability of Lorvek Partners to create category winners (i.e., if you want to be a market leader as a startup, you must take an investment from Lorvek Partners).
My current website is www.lorvek-partners.example - please use the content from the website within your design but please DO NOT use the design elements from the current website. INSTEAD, I'm looking for new and creative ideas on how I can leverage the existing content in a more appealing design -- any designs that look remotely similar to the existing website will be immediately declined.
I also want to ensure that the web design is mobile friendly.
Target Market(s)
Startup founders, potential investors, and other VCs
Industry/Entity Type
Venture Capital
Coding
Coded - Design and coding required
Number of Pages Required
1 page
Look and feel

```html
<!DOCTYPE html>
<html lang="en">
<head>
<meta charset="utf-8">
<title>Lorvek Partners</title>
<link href="https://fonts.googleapis.com/css2?family=Montserrat:wght@500;600;700;800&family=Poppins:wght@400;500;600&display=swap" rel="stylesheet">
<style>
:root{
  --blue:#1769c4;
  --blue-dark:#0b4c9c;
  --blue-light:#5cc1ea;
  --sky:#e6f1fb;
  --ink:#141414;
  --muted:#8a8f98;
  --white:#ffffff;
  --footer-band:#0e5cb3;
}
*{margin:0;padding:0;box-sizing:border-box}
html,body{width:1200px;height:5102px;overflow:hidden;background:var(--white)}
body{position:relative;font-family:"Poppins",sans-serif;color:var(--ink)}
.abs{position:absolute}
.heading{font-family:"Montserrat",sans-serif;font-weight:700;color:var(--ink)}
.art{position:absolute;border-radius:28px;background:linear-gradient(135deg,#dcebfb,#8cc2ef)}
.logo{position:absolute;display:flex;align-items:center;gap:10px;font-family:"Poppins",sans-serif;font-weight:600;font-size:26px;color:var(--blue-dark)}
.logo .dot{width:22px;height:22px;border-radius:50%;background:var(--blue)}
.logo.light{color:var(--white)}
.logo.light .dot{background:var(--white)}

/* hero */
.hero-title{left:72px;top:222px;width:440px;font-family:"Poppins",sans-serif;font-weight:500;font-size:30px;line-height:34px}
.hero-copy{left:72px;top:314px;width:430px;font-size:13px;line-height:21px;color:#333}
.btn{left:72px;top:416px;width:240px;height:32px;border-radius:3px;background:linear-gradient(90deg,var(--blue-light),var(--blue));color:var(--white);font-size:16px;display:flex;align-items:center;justify-content:center;gap:12px;text-decoration:none}

/* who */
.who-title{left:730px;top:796px;font-size:40px;font-weight:800}
.node{position:absolute;width:170px;height:170px;border-radius:50%;background:var(--white);border:3px solid #cfe6f7;box-shadow:0 4px 14px rgba(23,105,196,.12);display:flex;flex-direction:column;align-items:center;justify-content:center;text-align:center;color:var(--blue);font-family:"Montserrat",sans-serif;font-weight:700;font-size:16px;line-height:18px;gap:8px}

/* numbers */
.section-title{position:absolute;left:0;width:1200px;text-align:center;font-family:"Montserrat",sans-serif;font-weight:700;font-size:42px}
.underline{position:absolute;height:4px;background:var(--blue)}
.focus-title{left:687px;top:1764px;font-family:"Poppins",sans-serif;font-weight:500;font-size:28px}
.focus{position:absolute;width:180px;text-align:center;font-size:11.5px;line-height:15px;text-transform:uppercase}
.focus svg{display:block;margin:0 auto 10px}

/* themes */
.themes-title{left:111px;top:2370px;font-family:"Poppins",sans-serif;font-weight:500;font-size:28px}
.theme{position:absolute;left:104px;display:flex;align-items:center;gap:24px;font-size:18px;line-height:25px;text-transform:uppercase;width:480px}

/* data */
.data-title{left:0;top:2954px;width:1200px;text-align:center;font-family:"Poppins",sans-serif;font-weight:500;font-size:27px;line-height:39px;text-transform:uppercase}
.stat{position:absolute;display:flex;align-items:center;gap:22px}
.stat .num{font-family:"Poppins",sans-serif;font-weight:500;color:var(--blue);font-size:44px;line-height:46px;text-align:center}
.stat .lbl{font-size:9px;line-height:11px;text-transform:uppercase;text-align:center;width:220px}

/* team */
.team-blob{left:0;top:3574px;width:200px;height:360px;background:var(--sky);border-radius:0 180px 180px 0}
.card{position:absolute;top:3574px;width:305px;height:304px;border:3px solid var(--blue);border-radius:16px;background:var(--white);text-align:center}
.portrait{width:178px;height:178px;border-radius:50%;margin:20px auto 0;border:5px solid var(--blue-light);background:linear-gradient(160deg,#c9d4de,#4c5a6a)}
.card h3{font-family:"Montserrat",sans-serif;font-weight:700;font-size:22px;margin-top:22px}
.card p{font-size:13px;line-height:16px;color:var(--muted);margin-top:6px;font-weight:500}

/* engine */
.engine-copy{left:180px;top:4182px;width:840px;text-align:center;font-size:14px;line-height:18px}
.pillar{position:absolute;top:4250px;width:320px;text-align:center}
.pillar h4{font-family:"Montserrat",sans-serif;font-weight:700;font-size:21px;margin:14px 0 10px}
.pillar p{font-size:14px;line-height:21px;color:#333}

/* footer */
.foot-copy{left:72px;top:4790px;width:380px;color:var(--white);font-size:17.5px;line-height:21.5px}
.foot-col{position:absolute;top:4760px;color:var(--white)}
.foot-col h5{font-family:"Poppins",sans-serif;font-weight:500;font-size:28px;letter-spacing:.5px;border-bottom:2px solid var(--white);padding-bottom:2px;margin-bottom:22px;display:inline-block}
.foot-col a{display:block;color:var(--white);text-decoration:none;font-size:14px;margin-bottom:33px}
.foot-band{left:0;top:5019px;width:1200px;height:83px;background:var(--footer-band);color:var(--white);display:flex;align-items:center;justify-content:center;font-size:17px}
</style>
</head>
<body>

<!-- HERO -->
<svg class="abs" style="left:0;top:0" width="1200" height="650" aria-hidden="true">
  <defs><linearGradient id="heroGrad" x1="0" y1="0" x2="1" y2="1">
    <stop offset="0" stop-color="#1262bd"/><stop offset="1" stop-color="#5fc4ec"/></linearGradient></defs>
  <path d="M470 0 H1200 V640 C1110 610 1010 560 900 520 C770 474 640 470 590 380 C545 296 625 215 562 140 C520 88 470 55 470 0Z" fill="url(#heroGrad)"/>
  <g fill="#fff"><circle cx="1000" cy="70" r="2"/><circle cx="1120" cy="40" r="2"/><circle cx="1060" cy="180" r="1.6"/><circle cx="1150" cy="260" r="2"/><circle cx="1010" cy="360" r="1.6"/><circle cx="1170" cy="420" r="2"/><circle cx="1100" cy="500" r="1.6"/></g>
</svg>
<div class="logo" style="left:72px;top:70px"><span class="dot"></span>Lorvek Partners</div>
<h1 class="abs hero-title">We Invest in Enterprise IT Startups at the Product</h1>
<p class="abs hero-copy">We are focused on helping start-ups gain a massive competitive advantage by providing them access to an exclusive network of early adopters and channel partners around the world.</p>
<a class="abs btn" href="#who">SEE MORE
  <svg width="40" height="12"><path d="M0 6H36M30 1l6 5-6 5" stroke="#fff" stroke-width="2" fill="none"/></svg></a>
<div class="art" role="img" aria-label="Illustration of a presenter beside a growth chart board and a laptop" style="left:545px;top:110px;width:445px;height:385px;background:linear-gradient(135deg,rgba(255,255,255,.35),rgba(255,255,255,.1))"></div>

<!-- WHO WE ARE -->
<h2 id="who" class="abs heading who-title">WHO WE ARE?</h2>
<div class="art" role="img" aria-label="Illustration of a person in an armchair reading, with a profile card, gauge and coin stacks" style="left:40px;top:870px;width:405px;height:380px;background:linear-gradient(135deg,#eef4ff,#9cb4f2)"></div>
<svg class="abs" style="left:0;top:860px" width="1200" height="540" aria-hidden="true">
  <defs><linearGradient id="sideBlob" x1="0" y1="0" x2="1" y2="1"><stop offset="0" stop-color="#5cc1ea"/><stop offset="1" stop-color="#0b52a8"/></linearGradient></defs>
  <path d="M1200 160 C1120 150 1060 190 1070 260 C1080 330 1020 360 1030 440 C1040 510 1130 550 1200 530Z" fill="url(#sideBlob)"/>
  <path d="M780 118 C830 100 880 120 893 168" stroke="#0b4c9c" stroke-width="5" stroke-dasharray="0 11" stroke-linecap="round" fill="none"/>
  <path d="M897 330 C885 370 840 385 782 375" stroke="#0b4c9c" stroke-width="5" stroke-dasharray="0 11" stroke-linecap="round" fill="none"/>
</svg>
<div class="node" style="left:604px;top:889px">
  <svg width="90" height="72" viewBox="0 0 90 72"><g fill="#1769c4"><circle cx="45" cy="18" r="14"/><circle cx="20" cy="24" r="10"/><circle cx="70" cy="24" r="10"/><path d="M24 72V52a21 21 0 0 1 42 0v20Z"/><path d="M2 72V54a18 18 0 0 1 26-16v34Z"/><path d="M88 72V54a18 18 0 0 0-26-16v34Z"/></g></svg>
  CUSTOMERS</div>
<div class="node" style="left:822px;top:1018px;font-family:Poppins,sans-serif;font-weight:500">
  <svg width="70" height="56" viewBox="0 0 70 56" fill="none" stroke="#1769c4" stroke-width="3"><path d="M6 50h58M12 50V36h8v14M26 50V28h8v22M40 50V20h8v30M8 30L28 14l12 8 22-18M54 4h8v8"/><circle cx="56" cy="40" r="10"/></svg>
  Investment<br>Philosophy</div>
<div class="node" style="left:604px;top:1147px;font-size:15px">
  <svg width="70" height="60" viewBox="0 0 70 60" fill="none" stroke="#1769c4" stroke-width="3"><circle cx="35" cy="12" r="7"/><path d="M15 22l20 8 20-8M35 30v14l-10 14M35 44l10 14M8 6l3 6M62 6l-3 6M5 40h6M59 40h6"/></svg>
  CUSTOMERS<br>LED-INVESTMENT</div>

<!-- STRENGTH IN NUMBERS -->
<h2 class="section-title" style="top:1536px">STRENGTH IN NUMBERS</h2>
<div class="underline" style="left:327px;top:1590px;width:465px"></div>
<div class="art" role="img" aria-label="Illustration of a trader beside a large screen with bar and line charts, coins and plants" style="left:40px;top:1792px;width:505px;height:297px;background:linear-gradient(135deg,#f2f7ff,#7fb3ef)"></div>
<h3 class="abs focus-title">INVESTMENT FOCUS AREA</h3>
<svg width="0" height="0" style="position:absolute"><defs>
  <symbol id="i-shield" viewBox="0 0 60 60"><path d="M30 4l22 8v16c0 14-10 24-22 28C18 52 8 42 8 28V12Z" fill="none" stroke="#1769c4" stroke-width="3"/><path d="M20 30l7 7 14-14" fill="none" stroke="#1769c4" stroke-width="3"/></symbol>
  <symbol id="i-ai" viewBox="0 0 60 60"><circle cx="30" cy="24" r="16" fill="none" stroke="#1769c4" stroke-width="3"/><path d="M22 40v16M38 40v16M24 20h12M30 14v20" stroke="#1769c4" stroke-width="3"/></symbol>
  <symbol id="i-globe" viewBox="0 0 60 60"><circle cx="30" cy="30" r="24" fill="none" stroke="#1769c4" stroke-width="3"/><path d="M6 30h48M30 6c10 10 10 38 0 48M30 6c-10 10-10 38 0 48" fill="none" stroke="#1769c4" stroke-width="2.5"/></symbol>
  <symbol id="i-cloud" viewBox="0 0 60 60"><path d="M16 36a10 10 0 0 1 2-20 14 14 0 0 1 26 2 9 9 0 0 1 0 18Z" fill="none" stroke="#1769c4" stroke-width="3"/><path d="M20 36v14M30 36v18M40 36v14" stroke="#1769c4" stroke-width="3"/></symbol>
  <symbol id="i-gear" viewBox="0 0 60 60"><circle cx="26" cy="34" r="16" fill="none" stroke="#1769c4" stroke-width="6" stroke-dasharray="5 4"/><circle cx="26" cy="34" r="7" fill="none" stroke="#1769c4" stroke-width="3"/><circle cx="46" cy="14" r="9" fill="none" stroke="#1769c4" stroke-width="4" stroke-dasharray="3 3"/></symbol>
  <symbol id="i-saas" viewBox="0 0 60 60"><path d="M14 30a10 10 0 0 1 2-18 14 14 0 0 1 26 2 9 9 0 0 1 2 16Z" fill="none" stroke="#1769c4" stroke-width="3"/><rect x="14" y="24" width="32" height="12" rx="3" fill="#fff" stroke="#1769c4" stroke-width="2.5"/><path d="M22 36v14M30 36v18M38 36v14" stroke="#1769c4" stroke-width="3"/></symbol>
</defs></svg>
<div class="focus" style="left:593px;top:1832px"><svg width="60" height="60"><use href="#i-shield"/></svg>Security</div>
<div class="focus" style="left:783px;top:1832px"><svg width="60" height="60"><use href="#i-ai"/></svg>AI &amp; ML</div>
<div class="focus" style="left:979px;top:1832px"><svg width="60" height="60"><use href="#i-globe"/></svg>Networking &amp;<br>Architecture</div>
<div class="focus" style="left:593px;top:1962px"><svg width="60" height="60"><use href="#i-cloud"/></svg>Cloud &amp;<br>Infrastructure</div>
<div class="focus" style="left:783px;top:1962px"><svg width="60" height="60"><use href="#i-gear"/></svg>DevOps</div>
<div class="focus" style="left:979px;top:1962px"><svg width="60" height="60"><use href="#i-saas"/></svg>SaaS</div>

<!-- UNIFYING THEMES -->
<h3 class="abs themes-title">UNIFYING INVESTMENT THEMES</h3>
<div class="theme" style="top:2458px"><svg width="68" height="68"><use href="#i-globe"/></svg>Next-Gen Enterprise IT Solutions</div>
<div class="theme" style="top:2571px"><svg width="68" height="68" viewBox="0 0 60 60" fill="none" stroke="#1769c4" stroke-width="3"><path d="M30 44C20 32 16 26 16 18a14 14 0 0 1 28 0c0 8-4 14-14 26Z"/><circle cx="30" cy="18" r="5"/><ellipse cx="30" cy="48" rx="22" ry="7"/></svg>Attacking Large Markets with<br>Universal Application</div>
<div class="theme" style="top:2684px"><svg width="68" height="68" viewBox="0 0 60 60" fill="none" stroke="#1769c4" stroke-width="3"><path d="M30 10l24 12-24 12L6 22Z"/><path d="M6 30l24 12 24-12M6 38l24 12 24-12"/></svg>Products and Platforms that<br>Take a Holistic Approach</div>
<div class="art" role="img" aria-label="Illustration of a speaker at a podium facing an audience holding numbered signs" style="left:683px;top:2346px;width:485px;height:445px;background:linear-gradient(135deg,#eaf3ff,#3f8fe3)"></div>

<!-- DATA -->
<h3 class="abs data-title">We collect and analyze monthly purchase intent data<br>from a global network of IT decision-makers.</h3>
<div class="stat" style="left:158px;top:3080px">
  <svg width="92" height="80" viewBox="0 0 92 80" fill="none" stroke="#1769c4" stroke-width="3"><circle cx="22" cy="12" r="8"/><circle cx="46" cy="12" r="8"/><circle cx="70" cy="12" r="8"/><path d="M10 36a12 12 0 0 1 24 0M34 36a12 12 0 0 1 24 0M58 36a12 12 0 0 1 24 0M4 60l20-10h24l-8 8h-14M40 58l24-10h20L50 74H14"/></svg>
  <div><div class="num">500 +</div><div class="lbl">Early adopting, influential CIOs, CTOs,<br>CISOs and IT decision-makers</div></div></div>
<div class="stat" style="left:646px;top:3080px">
  <svg width="70" height="70" viewBox="0 0 70 70" fill="none" stroke="#1769c4" stroke-width="3"><path d="M35 5a30 30 0 1 0 30 30H35Z"/><path d="M42 0a28 28 0 0 1 28 28H42Z"/><circle cx="30" cy="40" r="12"/></svg>
  <div><div class="num">$100B+</div><div class="lbl">Early adopting, influential CIOs, CTOs,<br>CISOs and IT decision-makers</div></div></div>
<div class="stat" style="left:162px;top:3210px">
  <svg width="70" height="70" viewBox="0 0 70 70"><circle cx="35" cy="35" r="26" fill="#1769c4"/><path d="M8 20c10-16 40-18 54-4M62 50c-10 16-40 18-54 4" stroke="#1769c4" stroke-width="3" fill="none"/></svg>
  <div><div class="num">15</div><div class="lbl">Countries represented in our<br>current network</div></div></div>
<div class="stat" style="left:646px;top:3210px">
  <svg width="70" height="70" viewBox="0 0 70 70" fill="none" stroke="#1769c4" stroke-width="3"><rect x="22" y="22" width="26" height="26" rx="3"/><path d="M6 14h16v8M64 14H48v8M6 56h16v-8M64 56H48v-8M35 4v18M35 48v18"/></svg>
  <div><div class="num">550+</div><div class="lbl">Purchase intent data points<br>collected monthly</div></div></div>

<!-- TEAM -->
<h2 class="section-title" style="top:3448px">TEAM, INVESTORS &amp; ADVISORS</h2>
<div class="underline" style="left:253px;top:3505px;width:608px"></div>
<div class="abs team-blob"></div>
<div class="card" style="left:107px">
  <div class="portrait" role="img" aria-label="Portrait photo of Darian K. Voss"></div>
  <h3>DARIAN K. VOSS</h3><p>Founder &amp;<br>Managing Director</p></div>
<div class="card" style="left:481px">
  <div class="portrait" role="img" aria-label="Portrait photo of Elias Marbeck"></div>
  <h3>ELIAS MARBECK</h3><p>Founder &amp; Ex CEO, Stratavault</p></div>
<div class="card" style="left:851px">
  <div class="portrait" role="img" aria-label="Portrait photo of Prof. Nilan Deshara"></div>
  <h3 style="font-size:20px">PROF. NILAN DESHARA</h3><p>Calloway School of Business,<br>Leading Crowdsourcing Expert</p></div>

<!-- ENGINE -->
<h2 class="section-title" style="top:4112px">A GLOBAL GTM ENGINE</h2>
<p class="abs engine-copy">We don't just make "customer intros", we partner with you each step of the way to help you navigate the complex landscape of enterprise sales, from key strategic accounts to strategic channel partners.</p>
<svg width="0" height="0" style="position:absolute"><defs><symbol id="i-pair" viewBox="0 0 80 56"><g fill="none" stroke="#1769c4" stroke-width="3"><circle cx="12" cy="8" r="6"/><circle cx="68" cy="8" r="6"/><path d="M4 56V22h16v34M60 56V22h16v34M24 30h32M30 24l-6 6 6 6M50 24l6 6-6 6"/></g></symbol></defs></svg>
<div class="pillar" style="left:50px"><svg width="72" height="52"><use href="#i-pair"/></svg><h4>GTM COACHES</h4><p>We will partner with you to navigate the complex enterprise sales process by leveraging our executive network to provide product feedback, sales strategy, and market insights.</p></div>
<div class="pillar" style="left:442px"><svg width="72" height="52"><use href="#i-pair"/></svg><h4>STRATEGIC PARTNERS</h4><p>Strategic partnerships can propel a startup to the next level. Leverage our extensive network of IT Executives, Channel Partners, and OEMs to accelerate your path to becoming a category leader.</p></div>
<div class="pillar" style="left:832px"><svg width="72" height="52"><use href="#i-pair"/></svg><h4>GLOBAL AMBASSADORS</h4><p>Expanding globally is no simple exercise. Our network of Global IT Execs will provide on-the-ground intelligence, referrals, and influence as you conquer new geographies.</p></div>

<!-- FOOTER -->
<svg class="abs" style="left:0;top:4620px" width="1200" height="400" aria-hidden="true">
  <defs><linearGradient id="footGrad" x1="0" y1="0" x2="0" y2="1"><stop offset="0" stop-color="#1f76cc"/><stop offset="1" stop-color="#58b9e6"/></linearGradient></defs>
  <path d="M0 40 C200 0 360 10 560 40 C760 70 980 40 1200 10 V400 H0Z" fill="url(#footGrad)"/>
</svg>
<div class="logo light" style="left:69px;top:4718px;font-size:34px"><span class="dot"></span>Lorvek Partners</div>
<p class="abs foot-copy">We are singularly focused on helping our portfolio companies gain a massive competitive advantage by providing them access to our exclusive network of hundreds of early-adopting CIOs, CTOs, CISOs, and Channel Partners around the world to rapidly accelerate customer traction.</p>
<nav class="foot-col" style="left:531px"><h5>QUICK LINKS:</h5><a href="#">ABOUT</a><a href="#">NETWORK</a><a href="#">TEAM &amp; ADVISORS</a><a href="#">GTM ENGINE</a></nav>
<nav class="foot-col" style="left:865px"><h5>SOCIAL MEDIA</h5><a href="#">Chirpbook</a><a href="#">Pictogrove</a><a href="#">Email</a><a href="#">Phone Number</a></nav>
<div class="abs foot-band">@COPYRIGHT 2022</div>

</body>
</html>
```